Postcard double sided

Title: DWIGHT'S REVENGE

Why would Dwight Kersting align himself with Gordon Tasker?

(photo of two guys)

Dwight approached elected officials that he wanted to run for office, but did not have money to finance his campaign. He wanted other elected officials to finance his campaign. Everyone told him that they would help him get the vote out, but that he needed to finance his own race.

In comes Gordon Tasker.

Gordon Tasker who has a pay to play scheme over at the City, told Dwight he would finance his campaign on one condition.

He needed to run against Stuart Hobbs.

Why would Dwight want to run with no money?

Backside

DWIGHT'S REVENGE

Dwight decided to run because no one on the school board would terminate Dwight's ex and her new boyfriend who both work for the school district. His ex even filed criminal charges against him that are still pending.

Mug Shot facing left (name the charges Criminal Trespass , and Criminal Mischief (highlight bold letters use two lines) mug shot facing right

Complaint one (then photo with full face) Compliant 2)
(showcharges)

Dwight's ultimate goal is to terminate his ex and her new boyfriend if elected.
Plus Gordon Tasker needs the majority on the school board to do what he does bet.

Kickbacks for Contracts.

They will hire their own contractors!
Say "No" to Dwight's Revenge and Gordon Tasker Money Grab!

Title On Back: all caps: DOMESTIC VIOLENCE

```html
<!DOCTYPE html>
<html lang="en">
<head>
<meta charset="utf-8">
<title>Dwight's Revenge – Postcard</title>
<link rel="stylesheet" href="https://fonts.googleapis.com/css2?family=Anton&family=Oswald:wght@300;400;600;700&display=swap">
<style>
  :root{
    --blue:#00a8cc;
    --yellow:#fff200;
    --ink:#111111;
    --white:#ffffff;
    --pale-blue:#c6e6ee;
    --page:#e4e4e2;
    --photo-blue:#2d4a6b;
    --photo-gray:#8e99a3;
  }
  *{box-sizing:border-box;margin:0;padding:0}
  html,body{width:1200px;height:1200px;overflow:hidden;background:var(--page)}
  .canvas{position:relative;width:1200px;height:1200px}
  .card{position:absolute;top:268px;width:488px;height:631px;background:var(--white);overflow:hidden;box-shadow:0 4px 14px rgba(0,0,0,.18);font-family:"Oswald",sans-serif;color:var(--ink)}
  .card--front{left:59px}
  .card--back{left:630px}
  .abs{position:absolute}
  .title{top:14px;left:0;width:100%;text-align:center;font-family:"Anton",sans-serif;font-size:60px;line-height:70px;color:var(--blue);white-space:nowrap;letter-spacing:-.5px}
  .blue{color:var(--blue)} .yel{color:var(--yellow)} .wht{color:var(--white)} .b{font-weight:600}

  /* front */
  .intro-band{top:94px;left:0;width:488px;height:302px;background:var(--blue)}
  .question{top:110px;left:18px;font-family:"Oswald",sans-serif;font-weight:700;font-size:25px;line-height:31.4px;text-transform:uppercase}
  .duo-photo{top:94px;left:125px;width:210px;height:302px;background:linear-gradient(180deg,var(--photo-blue),#1d2f45 60%,#3a3a3a)}
  .story{top:104px;left:350px;width:130px;font-weight:300;font-size:13px;line-height:16.4px;color:var(--ink);text-transform:uppercase}
  .story p{margin-bottom:5px}
  .story .b{font-weight:600}
  .handshake{top:428px;left:18px;width:92px;height:66px}
  .deal{top:410px;left:127px;width:350px;font-weight:300;font-size:15.5px;line-height:19.5px;text-transform:uppercase}
  .deal .lead{font-weight:600;margin-bottom:4px}
  .deal .cond{font-weight:600;color:var(--blue);margin-top:5px}
  .cta-band{left:0;width:488px;background:var(--yellow)}
  .cta-band--front{top:524px;height:107px}
  .cta{font-family:"Anton",sans-serif;text-transform:uppercase;line-height:40px;white-space:nowrap}
  .cta--front{top:20px;left:22px;font-size:36px}
  .wallet{top:532px;left:397px;width:70px;height:80px}

  /* back */
  .reason{top:90px;left:29px;width:205px;font-weight:300;font-size:13px;line-height:16.8px;text-transform:uppercase}
  .siren{top:176px;left:28px;width:46px;height:48px}
  .pending{top:186px;left:80px;width:160px;font-weight:300;font-size:13px;line-height:16.8px;text-transform:uppercase}
  .mug{top:111px;width:89px;height:83px;background:linear-gradient(180deg,#cfd6da,#9aa5ad);border:1px solid var(--blue)}
  .mug--left{left:245px} .mug--right{left:366px}
  .charge{top:191px;height:19px;padding:0 6px;background:var(--yellow);font-size:11.5px;line-height:19px;text-transform:uppercase;font-weight:400;white-space:nowrap}
  .charge--left{left:240px} .charge--right{left:362px}
  .amp{top:184px;left:344px;font-size:20px;font-weight:300}
  .evidence-band{top:279px;left:0;width:488px;height:125px;background:var(--pale-blue)}
  .complaint-label{top:246px;font-family:"Oswald",sans-serif;font-weight:700;font-size:14px;color:var(--blue);text-transform:uppercase}
  .complaint-label--one{left:70px} .complaint-label--two{left:342px}
  .doc{top:266px;width:118px;height:152px;background:#fbfbfb;border:1px solid var(--blue)}
  .doc--one{left:48px;transform:rotate(-3deg)}
  .doc--two{left:322px;transform:rotate(3deg)}
  .front-mug{top:286px;left:189px;width:110px;height:112px;background:linear-gradient(180deg,#c8cdd1,#7f8a92 70%,#2c3a33)}
  .goal{top:420px;left:0;width:488px;text-align:center;font-weight:300;font-size:12.5px;line-height:16px;text-transform:uppercase}
  .goal p{margin-bottom:4px}
  .goal .b{font-weight:600}
  .goal .kick{color:var(--blue);font-weight:600;margin-top:5px}
  .cta-band--back{top:536px;height:95px}
  .cta--back{top:8px;left:0;width:488px;text-align:center;font-size:34px}
</style>
</head>
<body>
<div class="canvas">

  <section class="card card--front" aria-label="Postcard front">
    <h1 class="abs title">DWIGHT'S REVENGE</h1>
    <div class="abs intro-band"></div>
    <h2 class="abs question">Why<br>would<br><span class="yel">Dwight</span><br><span class="yel">Kersting</span><br>align<br>himself<br>with<br><span class="wht">Gordon</span><br><span class="wht">Tasker?</span></h2>
    <div class="abs duo-photo" role="img" aria-label="Photo of Dwight Kersting and Gordon Tasker standing together in suits at a campaign event"></div>
    <div class="abs story">
      <p>Dwight approached elected officials that <span class="b wht">he wanted to run for office</span>, but <span class="b yel">did not have money to finance his campaign.</span></p>
      <p class="b">He wanted other elected officials to finance his campaign.</p>
      <p><span class="b yel">Everyone told him</span> that they would help him get the vote out, but that <span class="b wht">he needed to finance his own race.</span></p>
    </div>
    <svg class="abs handshake" viewBox="0 0 92 66" fill="none" stroke="var(--blue)" stroke-width="4" stroke-linejoin="round" stroke-linecap="round" aria-hidden="true">
      <path d="M4 14 L20 6 L30 26 L14 34 Z"/>
      <path d="M88 14 L72 6 L62 26 L78 34 Z"/>
      <path d="M26 12 C36 8 44 10 52 14 L40 24 C36 27 42 32 48 28 L60 20 L68 26"/>
      <path d="M16 34 L40 58 C44 62 50 60 48 54 M34 50 L44 60 C50 62 54 56 50 52 M42 44 L54 56 C58 58 62 52 58 48 L44 36 M66 28 L72 32 L60 48"/>
    </svg>
    <div class="abs deal">
      <p class="lead">In comes Gordon Tasker.</p>
      <p><span class="blue">Gordon Tasker</span> who has a pay to play scheme over at the city, told Dwight <span class="blue">he would finance his campaign on one condition.</span></p>
      <p class="cond">He needed to run against Stuart Hobbs.</p>
    </div>
    <div class="abs cta-band cta-band--front">
      <p class="abs cta cta--front">Why would Dwight want<br>to run with <span class="blue">no money?</span></p>
    </div>
    <svg class="abs wallet" viewBox="0 0 70 80" fill="none" stroke="var(--ink)" stroke-width="4" stroke-linejoin="round" aria-hidden="true">
      <rect x="18" y="4" width="34" height="22" transform="rotate(18 35 15)" fill="var(--yellow)"/>
      <rect x="6" y="24" width="58" height="48" rx="8" fill="var(--yellow)"/>
      <rect x="44" y="40" width="20" height="16" rx="4"/>
      <path d="M14 32 L50 74 M50 30 L12 74" stroke="var(--blue)" stroke-width="9" stroke-linecap="round"/>
    </svg>
  </section>

  <section class="card card--back" aria-label="Postcard back">
    <h1 class="abs title">DWIGHT'S REVENGE</h1>
    <p class="abs reason">Dwight decided to run because no one on the school board would terminate Dwight's ex and her new boyfriend who both work for the school district.</p>
    <svg class="abs siren" viewBox="0 0 46 48" fill="none" stroke="var(--blue)" stroke-width="3.5" stroke-linecap="round" stroke-linejoin="round" aria-hidden="true">
      <path d="M12 40 V26 A11 11 0 0 1 34 26 V40"/>
      <rect x="6" y="40" width="34" height="6" rx="1"/>
      <path d="M23 2 V8 M6 9 L10 13 M40 9 L36 13 M1 24 H6 M40 24 H45"/>
    </svg>
    <p class="abs pending">His ex even filed criminal charges against him that are still pending.</p>
    <div class="abs mug mug--left" role="img" aria-label="Booking photo, profile facing left"></div>
    <div class="abs mug mug--right" role="img" aria-label="Booking photo, profile facing right"></div>
    <span class="abs charge charge--left">Criminal Trespass</span>
    <span class="abs amp">&amp;</span>
    <span class="abs charge charge--right">Criminal Mischief</span>
    <div class="abs evidence-band"></div>
    <p class="abs complaint-label complaint-label--one">Complaint 1</p>
    <p class="abs complaint-label complaint-label--two">Complaint 2</p>
    <div class="abs doc doc--one" role="img" aria-label="Scan of criminal complaint document one"></div>
    <div class="abs front-mug" role="img" aria-label="Front-facing booking photo"></div>
    <div class="abs doc doc--two" role="img" aria-label="Scan of criminal complaint document two"></div>
    <div class="abs goal">
      <p>Dwight's ultimate goal is to <span class="b">terminate<br>his ex &amp; her new boyfriend if elected.</span></p>
      <p>Plus Gordon Tasker needs<br><span class="b">the majority on the school board</span> to do what he does best.</p>
      <p class="kick">Kickbacks for contracts.</p>
      <p class="b">They will hire their own contractors!</p>
    </div>
    <div class="abs cta-band cta-band--back">
      <p class="abs cta cta--back">Say <span class="blue">“No”</span> to Dwight's Revenge &amp;<br>Gordon Tasker <span class="blue">money grab</span>!</p>
    </div>
  </section>

</div>
</body>
</html>
```